Startup but Passionate F&B Company with big dreams for the future and multiple brands needs business

We need a simple logo and typography design for business card usage for a new company in a bustling and modern city called Marlowe Quay Pte Ltd. We are an F&B company that owns multiple brands of small boutique and indie cafes and eateries. We offer artisanal and home made food created with passion using quality and fresh ingredient. We would like to remain relevant and grow in the future constantly adapting changes and testing new boundaries with our menu and offerings in line with moving tastes and times. Final design and colors should be simple, fresh but modern and will remain relevant in time to come. For fonts we prefer modern fonts such as avenir (meaning future/futuristic) or any other new and trendy font types.
Updates

Please include a logo design as well as typography on th name card.

Thanks

Industry/Entity Type

Boutique

Font styles to use
Other font styles liked:
• Avenir or any other modern looking fonts

Colors

Designer to choose colors to be used in the design.

Requirements
Must have
• Logo + typography

```html
<!DOCTYPE html>
<html lang="en">
<head>
<meta charset="utf-8">
<title>Marlowe Quay Pte Ltd — Business Card</title>
<link rel="stylesheet" href="https://fonts.googleapis.com/css2?family=Exo+2:wght@500;600&family=Open+Sans:wght@400;600&display=swap">
<style>
  :root {
    --indigo: #3e3f96;
    --charcoal: #2f2f33;
    --frame: #9c9c9c;
    --paper: #f7f7f7;
    --paper-edge: #e9e9e9;
    --ink: #2b2b2b;
    --backdrop: #8f8f8f;
    --white: #ffffff;
  }
  * { box-sizing: border-box; margin: 0; padding: 0; }
  html, body { width: 1200px; height: 895px; overflow: hidden; }
  body {
    background: var(--backdrop);
    position: relative;
    font-family: "Open Sans", Arial, sans-serif;
  }
  .card {
    position: absolute;
    top: 293px;
    width: 540px;
    height: 309px;
    background: radial-gradient(circle at 50% 40%, var(--white), var(--paper) 55%, var(--paper-edge));
    overflow: hidden;
  }
  .card--front { left: 40px; }
  .card--back { left: 620px; }
  .card__frame {
    position: absolute;
    left: 16px; top: 16px; right: 16px; bottom: 16px;
    border: 3px solid var(--frame);
  }
  .card__band {
    position: absolute;
    left: 0; right: 0;
    background: var(--indigo);
  }
  .company-name {
    position: absolute;
    font-family: "Exo 2", "Trebuchet MS", sans-serif;
    font-weight: 600;
    color: var(--indigo);
    letter-spacing: 0.5px;
    white-space: nowrap;
  }

  /* Front */
  .card--front .card__band { top: 210px; height: 58px; }
  .card--front .company-name { left: 150px; top: 112px; font-size: 27px; }
  .front__web {
    position: absolute;
    left: 0; right: 0; top: 226px;
    text-align: center;
    color: var(--white);
    font-size: 19px;
    letter-spacing: 1.5px;
  }

  /* Back */
  .card--back .card__band { top: 262px; height: 34px; }
  .back__accent {
    position: absolute;
    left: 0; top: 228px;
    width: 150px; height: 34px;
    background: var(--charcoal);
  }
  .back__accent-band {
    position: absolute;
    left: 150px; right: 0; top: 228px; height: 34px;
    background: var(--indigo);
  }
  .card--back .company-name { left: 34px; top: 30px; font-size: 21px; }
  .contact {
    position: absolute;
    display: flex;
    align-items: flex-start;
    gap: 9px;
    font-size: 13px;
    line-height: 17px;
    color: var(--ink);
  }
  .contact__icon {
    flex: none;
    width: 20px; height: 20px;
    border-radius: 4px;
    background: var(--indigo);
    display: flex; align-items: center; justify-content: center;
  }
  .contact__icon svg { width: 13px; height: 13px; }
  .contact--phone { left: 34px; top: 90px; }
  .contact--email { left: 34px; top: 120px; }
  .contact--address { left: 270px; top: 160px; }
  .contact--web { left: 270px; top: 198px; }
  .person {
    position: absolute;
    right: 38px; top: 88px;
    text-align: center;
    font-family: "Exo 2", "Trebuchet MS", sans-serif;
    color: var(--indigo);
  }
  .person__name { font-size: 19px; font-weight: 600; letter-spacing: 0.5px; }
  .person__role { font-size: 13px; font-weight: 500; letter-spacing: 0.5px; }
</style>
</head>
<body>

  <section class="card card--front" aria-label="Card front">
    <div class="card__frame"></div>
    <div class="company-name">Marlowe Quay Pte Ltd.</div>
    <div class="card__band"></div>
    <div class="front__web">www.marlowequay.com</div>
  </section>

  <section class="card card--back" aria-label="Card back">
    <div class="card__frame"></div>
    <div class="back__accent"></div>
    <div class="back__accent-band"></div>
    <div class="card__band"></div>

    <div class="company-name">Marlowe Quay Pte Ltd.</div>

    <div class="contact contact--phone">
      <span class="contact__icon">
        <svg viewBox="0 0 24 24" fill="#fff"><path d="M6.6 10.8a15.1 15.1 0 0 0 6.6 6.6l2.2-2.2a1 1 0 0 1 1-.25 11.4 11.4 0 0 0 3.6.57 1 1 0 0 1 1 1V20a1 1 0 0 1-1 1A17 17 0 0 1 3 4a1 1 0 0 1 1-1h3.5a1 1 0 0 1 1 1c0 1.25.2 2.45.57 3.57a1 1 0 0 1-.25 1z"/></svg>
      </span>
      <span>014 628 3391</span>
    </div>

    <div class="contact contact--email">
      <span class="contact__icon">
        <svg viewBox="0 0 24 24" fill="none" stroke="#fff" stroke-width="2"><rect x="3" y="5" width="18" height="14" rx="1"/><path d="M3 6l9 7 9-7"/></svg>
      </span>
      <span>hello@marlowequay.com</span>
    </div>

    <div class="person">
      <div class="person__name">Adrian Kole</div>
      <div class="person__role">Production engineer</div>
    </div>

    <div class="contact contact--address">
      <span class="contact__icon">
        <svg viewBox="0 0 24 24" fill="#fff"><path d="M12 2a7 7 0 0 0-7 7c0 5.2 7 13 7 13s7-7.8 7-13a7 7 0 0 0-7-7zm0 9.5A2.5 2.5 0 1 1 12 6.5a2.5 2.5 0 0 1 0 5z"/></svg>
      </span>
      <span>27, 9th floor, Harbour<br>Lane Road QTR</span>
    </div>

    <div class="contact contact--web">
      <span class="contact__icon">
        <svg viewBox="0 0 24 24" fill="none" stroke="#fff" stroke-width="1.8"><circle cx="12" cy="12" r="9"/><path d="M3 12h18M12 3c3 3 3 15 0 18M12 3c-3 3-3 15 0 18"/></svg>
      </span>
      <span>www.marlowequay.com</span>
    </div>
  </section>

</body>
</html>
```